New Flyer Design Project

I would like to purchase a customized version of a design you have previously submitted - https://www.artmarketly.com/design/58210947
hi
would like the design about the some. just with our  details and logo
office number 01394528160
Mobil number 07821563047
web lunarsweep.ltd
email lunarsweep@postmerin.co.uk
on the back we would like to put a price list

```html
<!DOCTYPE html>
<html lang="en">
<head>
<meta charset="utf-8">
<title>Lunar Sweep Flyer – Front and Back</title>
<link rel="stylesheet" href="https://fonts.googleapis.com/css2?family=Baloo+2:wght@700;800&family=Montserrat:wght@500;600;700;800&display=swap">
<style>
  :root{
    --stage:#1c1c1c;
    --sky:#5a9be6;
    --sky-deep:#4a88dc;
    --navy:#2d46a9;
    --navy-ink:#23309a;
    --brand-blue:#2f6fd1;
    --pink:#ff0fa0;
    --white:#ffffff;
    --card-edge:#d5d9e4;
    --silver-a:#f4f5f7;
    --silver-b:#b9bcc3;
  }
  *{box-sizing:border-box;margin:0;padding:0}
  html,body{width:1200px;height:1200px;overflow:hidden;background:var(--stage)}
  .stage{position:relative;width:1200px;height:1200px}
  .side-label{position:absolute;top:154px;width:570px;text-align:center;color:var(--white);
    font:700 31px/1 "Montserrat",sans-serif}
  .side-label--front{left:24px}
  .side-label--back{left:603px}

  .page{position:absolute;top:206px;width:570px;height:738px;overflow:hidden;background:var(--sky)}
  .page--front{left:24px}
  .page--back{left:603px}
  .page-art{position:absolute;inset:0}

  /* front */
  .brand-pill{position:absolute;left:0;top:10px;width:312px;height:100px;
    background:rgba(255,255,255,.55);border-radius:0 50px 50px 0;padding:20px 0 0 38px}
  .brand-name{font:800 32px/1 "Montserrat",sans-serif;color:var(--brand-blue);letter-spacing:.5px}
  .brand-tag{margin-top:12px;font:500 14px/1 "Montserrat",sans-serif;color:var(--brand-blue);letter-spacing:.3px}

  .services{position:absolute;top:352px;left:35px;display:flex;gap:6px}
  .service-card{position:relative;width:164px;height:183px;background:var(--white);
    border:3px solid var(--card-edge);border-radius:9px;overflow:visible}
  .service-photo{display:block;margin:2px;width:154px;height:136px;border-radius:6px}
  .service-title{text-align:center;font:700 17px/1 "Baloo 2",sans-serif;color:var(--navy-ink);margin-top:10px}
  .service-tick{position:absolute;right:-6px;top:-14px;width:56px;height:50px}

  .intro{position:absolute;left:33px;top:545px;width:504px;color:var(--white);
    font:700 13.3px/1.27 "Montserrat",sans-serif;text-align:justify}
  .intro strong{color:var(--navy-ink);font-weight:800}

  .quote-bar{position:absolute;left:33px;top:624px;width:504px;height:40px;background:var(--pink);
    color:var(--white);text-align:center;font:800 22px/42px "Baloo 2",sans-serif;letter-spacing:.3px}

  .contact-web{position:absolute;left:33px;top:681px;color:var(--white);font:600 14px/1.25 "Montserrat",sans-serif}
  .contact-web div{display:flex;align-items:center;gap:3px}
  .contact-web svg{width:12px;height:12px}
  .contact-phones{position:absolute;left:286px;top:672px;color:var(--white)}
  .phone-row{display:flex;align-items:center;height:26px}
  .phone-label{width:54px;font:600 14.5px/1 "Montserrat",sans-serif}
  .phone-row svg{width:22px;height:22px;margin-right:13px}
  .phone-number{font:700 24px/1 "Montserrat",sans-serif}

  /* back */
  .price-pill{position:absolute;left:94px;top:29px;width:378px;height:86px;border-radius:43px;
    background:linear-gradient(90deg,#8cc6f4,#4f93e0);box-shadow:0 6px 14px rgba(20,30,90,.35);
    text-align:center;color:var(--white);font:800 45px/88px "Montserrat",sans-serif;letter-spacing:1px}
  .back-brand{position:absolute;left:40px;top:638px}
  .back-brand .brand-name{font-size:29px}
  .back-brand .brand-tag{margin-top:12px;font-size:13px}
</style>
</head>
<body>
<main class="stage">
  <h2 class="side-label side-label--front">Front</h2>
  <h2 class="side-label side-label--back">Back</h2>

  <!-- FRONT PAGE -->
  <section class="page page--front">
    <svg class="page-art" viewBox="0 0 570 738" aria-hidden="false">
      <defs>
        <linearGradient id="frontSky" x1="0" y1="0" x2="0" y2="1">
          <stop offset="0" stop-color="#6aa7ec"/><stop offset="1" stop-color="#4f8fe0"/>
        </linearGradient>
        <linearGradient id="heroTone" x1="0" y1="0" x2="1" y2="1">
          <stop offset="0" stop-color="#6d5a63"/><stop offset=".45" stop-color="#5e6f8f"/>
          <stop offset=".7" stop-color="#8aa3c4"/><stop offset="1" stop-color="#4f7a5a"/>
        </linearGradient>
        <linearGradient id="silver" x1="0" y1="0" x2="1" y2="0">
          <stop offset="0" stop-color="var(--silver-b)"/><stop offset=".5" stop-color="var(--silver-a)"/>
          <stop offset="1" stop-color="var(--silver-b)"/>
        </linearGradient>
      </defs>
      <rect width="570" height="738" fill="url(#frontSky)"/>
      <rect y="642" width="570" height="96" fill="var(--navy)"/>
      <path role="img" aria-label="Photo of a cleaner washing the windows of a brick building with a water-fed pole beside a white conservatory"
        d="M0 0H570V215C470 262 400 300 330 310C240 322 150 300 0 300Z" fill="url(#heroTone)"/>
      <path d="M0 298C150 298 240 320 330 308C400 298 470 258 570 212V232C470 282 400 316 330 326C240 340 150 318 0 312Z" fill="url(#silver)"/>
      <g fill="var(--white)">
        <circle cx="516" cy="266" r="1.6"/><circle cx="526" cy="266" r="1.6"/><circle cx="536" cy="266" r="1.6"/><circle cx="546" cy="266" r="1.6"/>
        <circle cx="516" cy="277" r="1.6"/><circle cx="526" cy="277" r="1.6"/><circle cx="536" cy="277" r="1.6"/><circle cx="546" cy="277" r="1.6"/>
        <circle cx="516" cy="288" r="1.6"/><circle cx="526" cy="288" r="1.6"/><circle cx="536" cy="288" r="1.6"/><circle cx="546" cy="288" r="1.6"/>
        <circle cx="516" cy="299" r="1.6"/><circle cx="526" cy="299" r="1.6"/><circle cx="536" cy="299" r="1.6"/><circle cx="546" cy="299" r="1.6"/>
        <circle cx="516" cy="310" r="1.6"/><circle cx="526" cy="310" r="1.6"/><circle cx="536" cy="310" r="1.6"/><circle cx="546" cy="310" r="1.6"/>
        <circle cx="516" cy="321" r="1.6"/><circle cx="526" cy="321" r="1.6"/><circle cx="536" cy="321" r="1.6"/><circle cx="546" cy="321" r="1.6"/>
      </g>
    </svg>

    <div class="brand-pill">
      <div class="brand-name">LUNAR SWEEP</div>
      <div class="brand-tag">CLEANING &amp; MAINTENANCE LTD</div>
    </div>

    <div class="services">
      <article class="service-card">
        <svg class="service-photo" viewBox="0 0 154 136" role="img" aria-label="Photo of a cleaner washing an office building's windows next to a work van">
          <defs><linearGradient id="svc1" x1="0" y1="0" x2="0" y2="1"><stop offset="0" stop-color="#8a5a4a"/><stop offset=".7" stop-color="#6b6f86"/><stop offset="1" stop-color="#9aa0a8"/></linearGradient></defs>
          <rect width="154" height="136" fill="url(#svc1)"/>
        </svg>
        <div class="service-title">Window Cleaning</div>
        <svg class="service-tick" viewBox="0 0 56 50"><path d="M4 28L20 44L52 4" fill="none" stroke="var(--pink)" stroke-width="9" stroke-linejoin="round"/></svg>
      </article>
      <article class="service-card">
        <svg class="service-photo" viewBox="0 0 154 136" role="img" aria-label="Photo of a gloved hand lifting leaves out of a gutter">
          <defs><linearGradient id="svc2" x1="0" y1="0" x2="1" y2="1"><stop offset="0" stop-color="#8fa276"/><stop offset=".5" stop-color="#5a4f3c"/><stop offset="1" stop-color="#9a9fa3"/></linearGradient></defs>
          <rect width="154" height="136" fill="url(#svc2)"/>
        </svg>
        <div class="service-title">Gutter Cleaning</div>
        <svg class="service-tick" viewBox="0 0 56 50"><path d="M4 28L20 44L52 4" fill="none" stroke="var(--pink)" stroke-width="9" stroke-linejoin="round"/></svg>
      </article>
      <article class="service-card">
        <svg class="service-photo" viewBox="0 0 154 136" role="img" aria-label="Photo of crazy-paving stones half cleaned by pressure washing">
          <defs><linearGradient id="svc3" x1="0" y1="0" x2="1" y2="1"><stop offset="0" stop-color="#5e5a48"/><stop offset=".5" stop-color="#a49e90"/><stop offset="1" stop-color="#6f6a5c"/></linearGradient></defs>
          <rect width="154" height="136" fill="url(#svc3)"/>
        </svg>
        <div class="service-title">Pressure Washing</div>
        <svg class="service-tick" viewBox="0 0 56 50"><path d="M4 28L20 44L52 4" fill="none" stroke="var(--pink)" stroke-width="9" stroke-linejoin="round"/></svg>
      </article>
    </div>

    <p class="intro"><strong>LUNAR SWEEP LTD</strong> have been cleaning windows for commercial and residential properties throughout Hutton, Shenfield and the surrounding areas since 1999. We cover most towns in Essex including Brentwood, Chelmsford, Romford, Loughton and Billericay.</p>

    <div class="quote-bar">FOR A FREE QUOTE PLEASE CONTACT</div>

    <div class="contact-web">
      <div><svg viewBox="0 0 12 12" fill="none" stroke="var(--white)" stroke-width="1"><circle cx="6" cy="6" r="5"/><ellipse cx="6" cy="6" rx="2.2" ry="5"/><path d="M1 6H11M2 3.5H10M2 8.5H10"/></svg>www.lunarsweep.ltd</div>
      <div><svg viewBox="0 0 12 12" fill="none" stroke="var(--white)" stroke-width="1"><rect x="1" y="2.5" width="10" height="7"/><path d="M1 2.5L6 7L11 2.5"/></svg>lunarsweep@postmerin.co.uk</div>
    </div>

    <div class="contact-phones">
      <div class="phone-row"><span class="phone-label">Office</span>
        <svg viewBox="0 0 24 24" fill="none" stroke="var(--white)" stroke-width="2" stroke-linecap="round"><path d="M5 3l3 0 2 5-2 1.5c1 2.5 3 4.5 5.5 5.5L15 13l5 2v3c0 1.5-1.5 3-3 2.8C10 19.5 4.5 14 3.2 7 3 5 4 3 5 3z"/><path d="M14 6a5 5 0 0 1 4 4M14 2.5a8.5 8.5 0 0 1 7.5 7.5"/></svg>
        <span class="phone-number">01394528160</span></div>
      <div class="phone-row"><span class="phone-label">Mobile</span>
        <svg viewBox="0 0 24 24" fill="none" stroke="var(--white)" stroke-width="2" stroke-linecap="round"><path d="M5 3l3 0 2 5-2 1.5c1 2.5 3 4.5 5.5 5.5L15 13l5 2v3c0 1.5-1.5 3-3 2.8C10 19.5 4.5 14 3.2 7 3 5 4 3 5 3z"/><path d="M14 6a5 5 0 0 1 4 4M14 2.5a8.5 8.5 0 0 1 7.5 7.5"/></svg>
        <span class="phone-number">07821563047</span></div>
    </div>
  </section>

  <!-- BACK PAGE -->
  <section class="page page--back">
    <svg class="page-art" viewBox="0 0 570 738">
      <defs>
        <linearGradient id="backPhoto" x1="0" y1="0" x2="1" y2="0">
          <stop offset="0" stop-color="#e8ecf5"/><stop offset=".4" stop-color="#b7c1dc"/><stop offset="1" stop-color="#6b79a6"/>
        </linearGradient>
      </defs>
      <rect width="570" height="738" fill="var(--sky)"/>
      <rect x="31" y="72" width="509" height="520" rx="30" fill="var(--navy)"/>
      <path d="M0 596C80 574 170 586 260 592C370 600 430 440 570 428V738H0Z" fill="var(--sky)"/>
      <path role="img" aria-label="Faded photo of a branded cleaning van parked outside a brick building"
        d="M0 608C80 586 170 598 260 604C370 612 430 456 570 442V738H0Z" fill="url(#backPhoto)"/>
    </svg>
    <div class="price-pill">PRICE LIST</div>
    <div class="back-brand">
      <div class="brand-name">LUNAR SWEEP</div>
      <div class="brand-tag">CLEANING &amp; MAINTENANCE LTD</div>
    </div>
  </section>
</main>
</body>
</html>
```